Business Card Design for Loft Pictures

Hi we need a business card designed for a new aerial photography business we have started, we use UAV Drones to take photos for corporate, events, real estate, local government etc , the business name is Loft Pictures Australia, we have a facebook page that might help you come up with some designs - https://www.facebook.com/loftpicturesaustralia

We need to have and editable AI file so that we can use different names and contact details. details for one of the cards as follow:

Ned Harrow
phone: 03 5521 4736
Mobile: 0431 957 284
email: ned@loftpicturez.example
web: www.loftpictures.example

have now changed: Designer Payment:Committed

Target Market(s)

We are a Aerial Photography business using Drones and UAV

Industry/Entity Type

Business

Logo Text

Loft Pictures Australia

Requirements
Must have
• Colors to match logo and be part of Loft Pictures Brand

```html
<!DOCTYPE html>
<html lang="en">
<head>
<meta charset="utf-8">
<title>Loft Pictures Australia – Business Card</title>
<link rel="stylesheet" href="https://fonts.googleapis.com/css2?family=Arimo&family=Michroma&display=swap">
<style>
  :root {
    --page-bg: #ffffff;
    --label-ink: #000000;
    --card-border: #8a8a8a;
    --brand-ink: #161616;
    --contact-ink: #4a4a4a;
    --rule: #7a7a7a;
    --front-light: #e6e6e6;
    --front-mid: #8c8c8c;
    --front-dark: #2e2e2e;
    --art-dark: #15151c;
    --art-blue: #1e2a7a;
  }
  * { box-sizing: border-box; margin: 0; padding: 0; }
  html, body { width: 971px; height: 1200px; overflow: hidden; background: var(--page-bg); }
  .sheet { position: relative; width: 971px; height: 1200px; }

  .side-label {
    position: absolute; left: 0; width: 100%; text-align: center;
    font-family: "Arimo", Arial, sans-serif; font-weight: 400; font-size: 58px; line-height: 1; color: var(--label-ink);
  }
  .side-label--front { top: 82px; }
  .side-label--back { top: 620px; }

  .card {
    position: absolute; left: 140px; width: 696px; overflow: hidden;
    font-family: "Michroma", Arial, sans-serif;
  }
  .card--front {
    top: 150px; height: 428px;
    background: radial-gradient(ellipse 75% 95% at 28% 18%, var(--front-light) 0%, var(--front-mid) 45%, var(--front-dark) 100%);
  }
  .card--back {
    top: 693px; height: 426px; background: #fff; border: 1px solid var(--card-border);
  }

  .dot-band {
    position: absolute; left: 0; right: 0; bottom: 0; height: 120px;
    background: linear-gradient(180deg, rgba(60,60,60,0) 0%, rgba(40,40,40,0.45) 100%);
  }
  .lens-art {
    position: absolute; top: 0; right: 0; width: 232px; height: 100%;
    background: linear-gradient(160deg, var(--art-dark) 0%, var(--art-blue) 55%, var(--art-dark) 100%);
  }

  .wordmark { position: absolute; color: var(--brand-ink); text-transform: uppercase; }
  .wordmark span { display: block; line-height: 1; }
  .wordmark__top { font-size: 70px; letter-spacing: 4px; }
  .wordmark__mid { font-size: 38px; margin-top: 14px; }
  .wordmark__sub { font-size: 17px; letter-spacing: 11px; margin-top: 20px; }

  .card--front .wordmark { left: 34px; top: 46px; }
  .card--back .wordmark { left: 0; right: 0; top: 116px; text-align: center; }
  .card--back .wordmark__sub { padding-left: 11px; }

  .contact { position: absolute; color: var(--contact-ink); text-transform: uppercase; font-size: 15px; letter-spacing: 3px; line-height: 23px; }
  .contact--name { left: 10px; top: 10px; }
  .contact--phones { right: 8px; top: 10px; text-align: right; }
  .contact--online { left: 0; right: 0; top: 366px; text-align: center; letter-spacing: 5px; line-height: 24px; }
  .rule { position: absolute; left: 33px; width: 628px; top: 352px; height: 2px; background: var(--rule); }
</style>
</head>
<body>
<main class="sheet">
  <h2 class="side-label side-label--front">Front</h2>
  <section class="card card--front">
    <div class="dot-band" role="img" aria-label="Decorative halftone dot band"></div>
    <div class="lens-art" role="img" aria-label="Camera lens illustration"></div>
    <div class="wordmark">
      <span class="wordmark__top">Loft</span>
      <span class="wordmark__mid">Pictures</span>
      <span class="wordmark__sub">Australia</span>
    </div>
  </section>

  <h2 class="side-label side-label--back">Back</h2>
  <section class="card card--back">
    <p class="contact contact--name">Ned Harrow</p>
    <p class="contact contact--phones">Phone: 03 5521 4736<br>Mobile: 0431 957 284</p>
    <div class="wordmark">
      <span class="wordmark__top">Loft</span>
      <span class="wordmark__mid">Pictures</span>
      <span class="wordmark__sub">Australia</span>
    </div>
    <div class="rule"></div>
    <p class="contact contact--online">Email: ned@loftpicturez.example<br>Web: www.loftpictures.example</p>
  </section>
</main>
</body>
</html>
```